Quillmont Billboard - Financial Services Company (Investments, Tax Planning and Insurance)

Our new office has a billboard directly above the office building. We'd like something eye-catching with a strong Call to Action, with the main part of the billboard being under 7 words if possible. We'd like you to include a way to get ahold of us (either our website quillmontllc.example or our phone number 302-418-2267. You may also include in small font something to indicate that we've been serving the area since 1980 (the DE area, the tri-state area, the Ashgrove Hollow, etc.)

We offer financial planning, tax planning, and insurance, and we help our clients to focus on their goals and happiness by providing everything they need for lifelong wealth under one roof.

Our logos are attached, we use a triangle logo with green and gray. We use the tagline "experience lifelong wealth" but this does not need to be included.

Potential ideas we have seen from other financial companies-
- the concept that the driver spends more time looking at billboards than planning for their retirement
-something along the lines of "everything you need for your finances is in this building right here" planning, investments, taxes, insurance"
-don't spend your time worrying about retirement, let us help you plan for it
-are you working for your money, or is it working for you?
- retirement takes planning, we're here to help
- ready to retire? talk to us
- need investment advice?
- need help investing?
- crossing your fingers isn't a retirement plan. we can help.
- retiring soon? you need help.

Those are just general ideas, please feel free to be creative.

brand colors:
#00b585
#00b185
#000000
#ffffff
#6d6f75
#6d6f75
#6f7074
#021712
#052e24

```html
<!DOCTYPE html>
<html lang="en">
<head>
<meta charset="utf-8">
<title>Quillmont Billboard – Retirement Takes Planning</title>
<link href="https://fonts.googleapis.com/css2?family=Anton&family=Poppins:wght@600;700;800&display=swap" rel="stylesheet">
<style>
  :root {
    --brand-green: #00a66e;
    --brand-gray: #6d6f75;
    --paper: #ffffff;
    --canvas-bg: #f4f4f4;
    --sky-light: #e4e9f0;
    --sky-mid: #b9c4d2;
    --sky-deep: #93a2b6;
  }
  html, body {
    margin: 0;
    width: 1200px;
    height: 1200px;
    overflow: hidden;
    background: var(--canvas-bg);
  }
  .stage {
    width: 1200px;
    height: 1200px;
    display: flex;
    align-items: center;
    justify-content: center;
  }
  .billboard {
    width: 1120px;
    height: 325px;
    display: block;
    box-shadow: 0 6px 18px rgba(0,0,0,0.18);
    background: var(--paper);
  }
  .headline-top { font-family: "Anton", sans-serif; fill: var(--brand-gray); }
  .headline-main { font-family: "Poppins", sans-serif; font-weight: 800; fill: var(--brand-green); }
  .subline { font-family: "Poppins", sans-serif; font-weight: 700; fill: var(--brand-gray); }
  .service { font-family: "Poppins", sans-serif; font-weight: 700; fill: var(--paper); }
  .phone-number { font-family: "Poppins", sans-serif; font-weight: 700; fill: var(--brand-gray); }
  .brand-name { font-family: "Poppins", sans-serif; font-weight: 600; fill: var(--brand-green); }
  .badge-small { font-family: "Poppins", sans-serif; font-weight: 600; fill: var(--brand-green); }
  .badge-year { font-family: "Poppins", sans-serif; font-weight: 700; fill: var(--brand-green); }
</style>
</head>
<body>
<main class="stage">
  <svg class="billboard" viewBox="0 0 1604 466" xmlns="http://www.w3.org/2000/svg">
    <defs>
      <linearGradient id="sky" x1="0" y1="0" x2="0" y2="1">
        <stop offset="0" stop-color="var(--sky-mid)"/>
        <stop offset="0.5" stop-color="var(--sky-light)"/>
        <stop offset="1" stop-color="var(--sky-deep)"/>
      </linearGradient>
    </defs>

    <rect class="board-bg" width="1604" height="466" fill="var(--paper)"/>

    <!-- photo panel -->
    <polygon class="photo-panel" role="img" aria-label="Photo of an older couple embracing, seen from behind, looking out over water under a cloudy sky"
      points="0,0 555,0 595,466 0,466" fill="url(#sky)"/>

    <!-- corner accents -->
    <polygon class="accent-gray" points="0,58 170,0 215,0 0,84" fill="var(--brand-gray)"/>
    <polygon class="accent-green" points="0,110 215,0 228,0 0,122" fill="var(--paper)"/>
    <polygon class="accent-green" points="60,58 175,0 225,0 0,110 0,84 215,0" fill="var(--brand-green)"/>
    <polygon class="accent-white" points="0,125 235,0 275,0 0,145" fill="var(--paper)"/>
    <polygon class="accent-white" points="0,395 130,466 100,466 0,410" fill="var(--paper)"/>
    <polygon class="accent-green" points="0,412 100,466 72,466 0,428" fill="var(--brand-green)"/>
    <polygon class="accent-gray" points="0,440 48,466 30,466 0,450" fill="var(--brand-gray)"/>

    <!-- divider bands -->
    <polygon class="divider-green" points="588,150 596,150 636,466 612,466" fill="var(--brand-green)"/>
    <polygon class="divider-gray" points="578,0 618,0 678,466 636,466" fill="var(--brand-gray)"/>

    <!-- since badge -->
    <g class="since-badge">
      <circle cx="466" cy="122" r="66" fill="var(--paper)" stroke="var(--brand-green)" stroke-width="4"/>
      <text class="badge-small" x="466" y="106" font-size="12" text-anchor="middle" letter-spacing="1">SINCE</text>
      <text class="badge-year" x="466" y="140" font-size="34" text-anchor="middle">1980</text>
    </g>

    <!-- headline -->
    <text class="headline-top" x="716" y="125" font-size="102" textLength="832" lengthAdjust="spacingAndGlyphs">RETIREMENT TAKES</text>
    <text class="headline-main" x="713" y="245" font-size="142" textLength="840" lengthAdjust="spacingAndGlyphs">PLANNING</text>
    <text class="subline" x="714" y="283" font-size="34" textLength="840" lengthAdjust="spacing">WE ARE HERE TO HELP YOU</text>

    <!-- services band -->
    <rect class="services-band" x="662" y="292" width="942" height="54" fill="var(--brand-green)"/>
    <text class="service" x="670" y="331" font-size="29" textLength="376" lengthAdjust="spacingAndGlyphs">• FINANCIAL PLANNING</text>
    <text class="service" x="1066" y="331" font-size="29" textLength="262" lengthAdjust="spacingAndGlyphs">• TAX PLANNING</text>
    <text class="service" x="1344" y="331" font-size="29" textLength="212" lengthAdjust="spacingAndGlyphs">• INSURANCE</text>

    <!-- phone -->
    <g class="phone-icon" fill="none" stroke="var(--brand-green)" stroke-width="4">
      <circle cx="722" cy="402" r="24"/>
      <path d="M712 390 q-2 10 6 20 q8 9 16 8 l2 -6 l-7 -4 l-4 3 q-6 -4 -9 -10 l3 -4 l-4 -7 z" fill="var(--brand-green)" stroke-width="1.5"/>
      <path d="M724 388 q8 1 10 10 M724 382 q13 2 16 16" stroke-width="2.5" stroke-linecap="round"/>
    </g>
    <text class="phone-number" x="774" y="424" font-size="66" textLength="496" lengthAdjust="spacingAndGlyphs">302-418-2267</text>

    <!-- brand -->
    <g class="brand">
      <rect x="1330" y="384" width="26" height="26" fill="var(--brand-green)"/>
      <text class="brand-name" x="1366" y="409" font-size="34">Quillmont</text>
    </g>
  </svg>
</main>
</body>
</html>
```